A modern, fresh introduction to Buddhism

I need a book cover for an A6 sized book to be used both for ebook and hard copy. The author is a young, modern Buddhist teacher of high standing who has written this short intro to Buddhism in an informal Q & As format using modern, accessible language to convey profound and meaningful ideas to the general public. The author is Tibetan, but teaches worldwide and is very personable and dynamic. The cover should portray this and have a fresh yet authentic feel to it (nothing new-agey!). Please see the author's websites www.torvanelmiro.org and www.wbrt.org for reference, but do not feel that the design must align completely with the website designs.

Target Market(s)

General public both in Europe and America and in Asia ranging from teenagers to the elderly. A really broad audience.

Industry/Entity Type

Teacher

Requirements
Must have
• Please include the following text that on the front cover:

A Breath of Quiet Rivers

By Venerable Tsomar Deleng

Please include the following on the back cover:

Yarkun Tselpa Publications (with attached logo above it)
Nice to have
• A simplistic, artistic, and modern look without any traditional religious images.
Should not have
• No buddha images or religious images. I would prefer a more simplistic, modern and artistic look.

```html
<!DOCTYPE html>
<html lang="en">
<head>
<meta charset="utf-8">
<title>A Breath of Quiet Rivers — Book Cover</title>
<link rel="stylesheet" href="https://fonts.googleapis.com/css2?family=Ubuntu:wght@700&family=Oswald:wght@300;400&display=swap">
<style>
  :root {
    --crimson-deep: #5a0a06;
    --crimson-mid: #8e1a0f;
    --crimson-light: #a4301e;
    --shadow-line: rgba(20, 0, 0, 0.55);
    --night: #060404;
    --title-white: #ffffff;
    --byline-grey: #9a9a9a;
    --line-white: rgba(255, 255, 255, 0.92);
  }
  html, body {
    margin: 0;
    padding: 0;
    overflow: hidden;
    background: var(--night);
  }
  .cover {
    position: relative;
    width: 782px;
    height: 1200px;
    overflow: hidden;
    background: var(--night);
  }
  .cover__drapes {
    position: absolute;
    inset: 0;
    background:
      linear-gradient(to bottom, rgba(6,4,4,0.35) 0%, rgba(6,4,4,0) 8%, rgba(6,4,4,0) 48%, rgba(6,4,4,0.85) 64%, var(--night) 74%),
      repeating-linear-gradient(to right,
        var(--crimson-deep) 0px,
        var(--crimson-mid) 14px,
        var(--crimson-light) 36px,
        var(--crimson-mid) 60px,
        var(--crimson-deep) 78px,
        var(--shadow-line) 84px,
        var(--crimson-deep) 88px);
  }
  .cover__emblem {
    position: absolute;
    left: 132px;
    top: 70px;
    width: 506px;
    height: 506px;
  }
  .cover__title {
    position: absolute;
    left: 0;
    right: 0;
    top: 950px;
    margin: 0;
    text-align: center;
    font-family: "Ubuntu", sans-serif;
    font-weight: 700;
    font-size: 31px;
    letter-spacing: 1.5px;
    text-transform: uppercase;
    color: var(--title-white);
  }
  .cover__byline {
    position: absolute;
    right: 72px;
    top: 1014px;
    margin: 0;
    font-family: "Oswald", sans-serif;
    font-weight: 400;
    font-size: 17px;
    letter-spacing: 2px;
    word-spacing: 4px;
    text-transform: uppercase;
    color: var(--byline-grey);
  }
</style>
</head>
<body>
  <main class="cover">
    <div class="cover__drapes"></div>

    <svg class="cover__emblem" viewBox="0 0 506 506" xmlns="http://www.w3.org/2000/svg">
      <rect x="123" y="60" width="260" height="360" rx="120"
            fill="rgba(150,40,28,0.55)" role="img"
            aria-label="Fine white line illustration of a seated figure with lotus flowers in an arched frame"/>
      <circle cx="253" cy="253" r="249" fill="none" stroke="var(--line-white)" stroke-width="2"/>
    </svg>

    <h1 class="cover__title">A Breath of Quiet Rivers</h1>
    <p class="cover__byline">By Venerable Tsomar Deleng</p>
  </main>
</body>
</html>
```